Business Card Design Project

Company Name - Kestrova Care

Wellness consulting and training company. Run through a medical centre.

Main colour themes are orange and blue, as in the logo. Want to replicate same effect with business cards.

To give a sense of freedom and potential as per the company name.

Want the business card to be in line with stationary design, which I have launched as well.

Double sided with design and colour on one side and details on other side.
Updates

Reason: Need business card and stationary design to be teed up.

Target Market(s)

35 to 65 age group.
New age and trendy

Industry/Entity Type

Training

Requirements
Must have
• Colours orange and blue as per logo
Nice to have
• Design to be similar to stationary design, letterhead and envelopes

```html
<!DOCTYPE html>
<html lang="en">
<head>
<meta charset="utf-8">
<title>Kestrova Care – Business Card</title>
<link rel="stylesheet" href="https://fonts.googleapis.com/css2?family=Montserrat:wght@500;600;700&family=Roboto+Condensed:wght@400&display=swap">
<style>
  :root {
    --blue: #1f5fa8;
    --blue-deep: #174f8f;
    --blue-light: #3a7cc4;
    --orange: #e8661e;
    --card: #ffffff;
    --card-shade: #eceef0;
    --ink: #1d1d1d;
    --backdrop: #2b2b2d;
  }
  * { box-sizing: border-box; margin: 0; padding: 0; }
  html, body {
    width: 1200px; height: 997px; overflow: hidden;
    background: var(--backdrop);
  }
  .stage { position: relative; width: 1200px; height: 997px; }

  .card {
    position: absolute;
    width: 560px; height: 320px;
    border-radius: 18px;
    overflow: hidden;
    background: linear-gradient(160deg, var(--card) 40%, var(--card-shade) 100%);
    box-shadow: 0 18px 40px rgba(0,0,0,.55);
  }

  /* Front side */
  .card--front { left: 90px; top: 110px; }
  .card--front .band {
    position: absolute; left: 0; top: 0; width: 100%; height: 50px;
    background: linear-gradient(90deg, var(--blue) 0%, var(--blue-light) 100%);
    border-bottom: 5px solid var(--orange);
  }
  .card--front .brand {
    position: absolute; left: 0; right: 0; top: 150px;
    display: flex; justify-content: center; align-items: center; gap: 14px;
  }
  .brand__name {
    font-family: "Roboto Condensed", sans-serif;
    font-weight: 400;
    color: var(--blue);
    letter-spacing: .5px;
  }
  .card--front .brand__name { font-size: 52px; }
  .brand__dot {
    width: 16px; height: 16px; border-radius: 50%; background: var(--orange);
  }

  /* Back side */
  .card--back { left: 550px; top: 560px; }
  .card--back .band {
    position: absolute; left: 0; bottom: 0; width: 100%; height: 70px;
    background: linear-gradient(90deg, var(--blue-light) 0%, var(--blue-deep) 100%);
    border-top: 5px solid var(--orange);
  }
  .card--back .brand {
    position: absolute; left: 30px; top: 140px;
    display: flex; align-items: center; gap: 10px;
  }
  .card--back .brand__name { font-size: 36px; }
  .card--back .brand__dot { width: 12px; height: 12px; }
  .divider {
    position: absolute; left: 282px; top: 30px; width: 3px; height: 200px;
    background: linear-gradient(180deg, rgba(31,95,168,0) 0%, var(--blue) 50%, rgba(31,95,168,0) 100%);
  }
  .details {
    position: absolute; left: 305px; top: 42px;
    font-family: "Montserrat", sans-serif;
  }
  .details__name { font-size: 17px; font-weight: 700; color: var(--blue); line-height: 1; }
  .details__role { font-size: 11px; font-weight: 600; color: var(--ink); margin: 3px 0 18px 12px; }
  .contact-list { list-style: none; }
  .contact-list li {
    display: flex; align-items: center; gap: 9px;
    font-size: 13px; font-weight: 500; color: var(--ink);
    margin-bottom: 9px;
  }
  .contact-list svg { width: 22px; height: 22px; flex: none; }
</style>
</head>
<body>
<main class="stage">

  <section class="card card--front" aria-label="Business card front">
    <div class="band"></div>
    <div class="brand">
      <span class="brand__name">Kestrova Care</span>
      <span class="brand__dot"></span>
    </div>
  </section>

  <section class="card card--back" aria-label="Business card back">
    <div class="brand">
      <span class="brand__name">Kestrova Care</span>
      <span class="brand__dot"></span>
    </div>
    <div class="divider"></div>
    <div class="details">
      <p class="details__name">YOUR NAME</p>
      <p class="details__role">Centre Director</p>
      <ul class="contact-list">
        <li>
          <svg viewBox="0 0 22 22" aria-hidden="true"><circle cx="11" cy="11" r="11" fill="#e8661e"/><path d="M6 8h10v2l-2 1v4H8v-4l-2-1z" fill="#fff"/></svg>
          +39 335 0142876
        </li>
        <li>
          <svg viewBox="0 0 22 22" aria-hidden="true"><circle cx="11" cy="11" r="11" fill="#e8661e"/><path d="M7 6.5c1-.8 1.8-.6 2.3.4l.7 1.5c.2.6 0 1-.5 1.4l-.6.4c.6 1.4 1.6 2.4 3 3l.4-.6c.4-.5.8-.7 1.4-.5l1.5.7c1 .5 1.2 1.3.4 2.3-1 1.2-2.6 1.2-4.4.2-2.1-1.2-3.7-2.8-4.6-4.8-.6-1.6-.5-3 .4-4z" fill="#fff"/></svg>
          (+123) 555 0199
        </li>
        <li>
          <svg viewBox="0 0 22 22" aria-hidden="true"><circle cx="11" cy="11" r="11" fill="#e8661e"/><rect x="5.5" y="7" width="11" height="8" fill="#fff"/><path d="M5.5 7l5.5 4.5L16.5 7" fill="none" stroke="#e8661e" stroke-width="1.2"/></svg>
          info@kestrovacare.com
        </li>
        <li>
          <svg viewBox="0 0 22 22" aria-hidden="true"><circle cx="11" cy="11" r="11" fill="#e8661e"/><g fill="none" stroke="#fff" stroke-width="1.8" stroke-linecap="round"><path d="M9.5 12.5l3-3"/><path d="M10 8.5l1-1a2.3 2.3 0 0 1 3.3 3.3l-1 1"/><path d="M12 13.5l-1 1a2.3 2.3 0 0 1-3.3-3.3l1-1"/></g></svg>
          www.kestrovacare.com
        </li>
      </ul>
    </div>
    <div class="band"></div>
  </section>

</main>
</body>
</html>
```